Letterhead to Introduce a 'Sister' Company.

What I am needing is a design for a letter head to introduce our current customers base of (KT Alarm) customers to our new service, 'Kestrel Tide Solar Brokers'

```html
<!DOCTYPE html>
<html lang="en">
<head>
<meta charset="utf-8">
<title>KT Alarm Letterhead</title>
<link rel="stylesheet" href="https://fonts.googleapis.com/css2?family=Montserrat:wght@400;800&family=Encode+Sans+Condensed:wght@400&family=Lato:wght@400&display=swap">
<style>
  :root {
    --brand-blue: #035598;
    --brand-blue-soft: #1a6aaa;
    --brand-green: #4cb848;
    --solar-orange: #f39a1e;
    --ink: #555555;
    --ink-dark: #5a5a5a;
    --paper: #ffffff;
  }
  * { margin: 0; padding: 0; box-sizing: border-box; }
  html, body { width: 1056px; height: 1200px; overflow: hidden; background: var(--paper); }
  .letterhead {
    position: relative;
    width: 1056px;
    height: 1200px;
    background: var(--paper);
    overflow: hidden;
    color: var(--ink);
  }
  .brand {
    position: absolute;
    display: flex;
    align-items: center;
    gap: 10px;
    font-family: "Montserrat", sans-serif;
    font-weight: 800;
  }
  .brand-primary {
    left: 100px;
    top: 108px;
    font-size: 40px;
    color: var(--brand-blue);
    letter-spacing: 1px;
  }
  .brand-primary .brand-dot {
    width: 18px; height: 18px; border-radius: 50%;
    background: var(--brand-green);
  }
  .brand-sister {
    right: 100px;
    top: 92px;
    flex-direction: column;
    align-items: center;
    gap: 8px;
    font-size: 24px;
    color: var(--brand-blue);
    text-align: center;
    line-height: 1.15;
  }
  .brand-sister .brand-dot {
    width: 34px; height: 34px; border-radius: 50%;
    background: var(--solar-orange);
  }
  .recipient {
    position: absolute;
    left: 100px;
    top: 282px;
    font-family: "Montserrat", sans-serif;
  }
  .letter-date { font-size: 20px; font-weight: 400; color: var(--ink); }
  .recipient-name {
    margin-top: 8px;
    font-size: 32px;
    font-weight: 800;
    color: var(--ink-dark);
    letter-spacing: 0.2px;
  }
  .recipient-title { margin-top: 8px; font-size: 20px; font-weight: 400; color: var(--ink); }
  .letter-body {
    position: absolute;
    left: 100px;
    top: 462px;
    width: 856px;
    font-family: "Encode Sans Condensed", sans-serif;
    font-size: 20.5px;
    line-height: 34px;
    color: var(--ink);
    text-align: justify;
  }
  .letter-body p + p { margin-top: 16px; }
  .closing {
    position: absolute;
    left: 100px;
    top: 790px;
    font-family: "Encode Sans Condensed", sans-serif;
    font-size: 21px;
    color: var(--ink);
  }
  .signature {
    position: absolute;
    left: 100px;
    top: 830px;
    width: 110px;
    height: 64px;
    background: linear-gradient(135deg, rgba(27,79,138,0.18), rgba(27,79,138,0.08));
    border-radius: 6px;
  }
  .footer-band {
    position: absolute;
    left: 0;
    bottom: 0;
    width: 1056px;
    height: 200px;
    background: linear-gradient(100deg, var(--brand-blue) 0%, var(--brand-blue) 55%, var(--brand-blue-soft) 80%, var(--brand-green) 100%);
  }
  .contact {
    position: absolute;
    left: 100px;
    top: 1040px;
    font-family: "Lato", sans-serif;
    font-style: normal;
    color: var(--paper);
    font-size: 20px;
    line-height: 24px;
  }
  .contact-address { margin-bottom: 10px; }
  .contact-line { display: flex; align-items: center; gap: 14px; height: 28px; }
  .contact-line svg { width: 20px; height: 20px; flex: none; }
</style>
</head>
<body>
<main class="letterhead">
  <div class="brand brand-primary"><span class="brand-name">KT Alarm</span><span class="brand-dot"></span></div>
  <div class="brand brand-sister"><span class="brand-dot"></span><span class="brand-name">Kestrel Tide<br>Solar Brokers</span></div>

  <section class="recipient">
    <p class="letter-date">10 December, 2021</p>
    <h1 class="recipient-name">DANIEL WHITFORD</h1>
    <p class="recipient-title">Cheif Executive Officer</p>
  </section>

  <section class="letter-body">
    <p>Contrary to popular belief, Lorem Ipsum is not simply random text. It has roots in a piece of classical Latin literature from 45 BC, making it over 2000 years old. Edward Hollis, a Latin professor at Linden-Hale College in Virginia, looked up one of the more obscure Latin words, consectetur.</p>
    <p>Lorem Ipsum comes from sections 1.10.32 and 1.10.33 of "de Finibus Bonorum et Malorum" (The Extremes of Good and Evil) by Aurelian Vell, written in 45 BC. This book is a treatise on the theory of ethics, very popular during the Renaissance. The first line of Lorem Ipsum.</p>
    <p>The standard chunk of Lorem Ipsum used since the 1500s is reproduced below for those interested.</p>
  </section>

  <p class="closing">Best Regards</p>
  <div class="signature" role="img" aria-label="Handwritten signature of Daniel Whitford"></div>

  <div class="footer-band" role="img" aria-label="Decorative blue and green wave band along the foot of the page"></div>

  <address class="contact">
    <p class="contact-address">PO Box 2270. Harborview,<br>WA 98020</p>
    <p class="contact-line">
      <svg viewBox="0 0 24 24"><path fill="#fff" d="M6.6 10.8c1.4 2.8 3.8 5.1 6.6 6.6l2.2-2.2c.3-.3.7-.4 1-.2 1.1.4 2.3.6 3.6.6.6 0 1 .4 1 1V20c0 .6-.4 1-1 1C10.6 21 3 13.4 3 4c0-.6.4-1 1-1h3.5c.6 0 1 .4 1 1 0 1.3.2 2.5.6 3.6.1.3 0 .7-.2 1L6.6 10.8z"/></svg>
      <span>888-555-0142</span>
    </p>
    <p class="contact-line">
      <svg viewBox="0 0 24 24"><rect x="2" y="5" width="20" height="14" fill="#fff"/><path d="M2 5l10 8 10-8M2 19l8-7M22 19l-8-7" stroke="var(--brand-blue)" stroke-width="1.5" fill="none"/></svg>
      <span>info@kthomesecurity.com</span>
    </p>
    <p class="contact-line">
      <svg viewBox="0 0 24 24" fill="none" stroke="#fff" stroke-width="1.5"><circle cx="12" cy="12" r="9"/><ellipse cx="12" cy="12" rx="4" ry="9"/><path d="M3 12h18M5 7h14M5 17h14"/></svg>
      <span>www.kthomesecurity.com</span>
    </p>
  </address>
</main>
</body>
</html>
```